Business Card Design for LeafCrest (Farming Devices)

We need Business Cards for our new Company based in Switzerland called "LeafCrest" We develop innovativ products for indoor and outdoor Farming for household and components for vertical farming. Our initial BloomNest gives people the possibility to grow their own food at home all year round. The design should communicate freshness, innovation, health.

```html
<!DOCTYPE html>
<html lang="en">
<head>
<meta charset="utf-8">
<title>LeafCrest Business Card</title>
<link href="https://fonts.googleapis.com/css2?family=Rubik:wght@400;500;700&display=swap" rel="stylesheet">
<style>
  :root {
    --backdrop: #8a8273;
    --card-white: #f3f4f5;
    --leaf-green: #6fb33f;
    --leaf-green-light: #78b946;
    --brand-blue: #0a72b9;
    --ink-white: #ffffff;
  }
  * { margin: 0; padding: 0; box-sizing: border-box; }
  html, body {
    width: 1200px; height: 1200px; overflow: hidden;
    background: var(--backdrop);
    font-family: "Rubik", sans-serif;
  }
  .stage { position: relative; width: 1200px; height: 1200px; }
  .card {
    position: absolute; left: 220px; width: 760px; height: 433px;
    border-radius: 20px; overflow: hidden;
    box-shadow: 0 12px 28px rgba(0,0,0,0.25);
  }
  .card-front { top: 147px; background: var(--card-white); }
  .card-back {
    top: 620px;
    background: linear-gradient(160deg, var(--leaf-green) 0%, var(--leaf-green-light) 100%);
    display: flex; align-items: center; justify-content: center;
  }
  .card-art { position: absolute; inset: 0; }
  .brand-name {
    position: absolute; left: 183px; top: 236px;
    transform: translate(-50%, -50%);
    font-weight: 500; font-size: 42px; color: var(--leaf-green);
    white-space: nowrap;
  }
  .back-brand-name {
    font-weight: 500; font-size: 66px; color: var(--ink-white);
    letter-spacing: 0.5px;
  }
  .contact-text {
    position: absolute; left: 437px; color: var(--ink-white);
    white-space: nowrap; font-weight: 500;
  }
  .person-name { top: 70px; font-size: 33px; font-weight: 700; }
  .person-title { top: 110px; font-size: 22px; font-weight: 400; }
  .contact-line { font-size: 22px; transform: translateY(-50%); }
  .phone-line { top: 226px; }
  .email-line { top: 290px; }
  .web-line { top: 353px; }
</style>
</head>
<body>
<div class="stage">
  <section class="card card-front">
    <svg class="card-art" width="760" height="433" viewBox="0 0 760 433" aria-hidden="true">
      <rect x="380" y="0" width="380" height="433" fill="#74b743"/>
      <path d="M352 0 H409 V118 Q409 128 398 132 L380 140 L362 132 Q352 128 352 118 Z" fill="#0a72b9"/>
      <path d="M352 210 Q352 200 362 196 L380 188 L398 196 Q409 200 409 210 V433 H352 Z" fill="#0a72b9"/>
      <!-- person -->
      <circle cx="380" cy="104" r="20" fill="#fff"/>
      <circle cx="380" cy="99" r="5" fill="#0a72b9"/>
      <path d="M371 113 Q371 105 380 105 Q389 105 389 113 Z" fill="#0a72b9"/>
      <!-- phone -->
      <circle cx="380" cy="226" r="20" fill="#fff"/>
      <path d="M373 217 l4 -2 l3 6 l-3 2 q2 5 6 7 l2 -3 l6 3 l-2 4 q-10 1 -16 -17 z" fill="#0a72b9"/>
      <!-- home -->
      <circle cx="380" cy="290" r="20" fill="#fff"/>
      <path d="M369 291 L380 281 L391 291 L388 291 L388 299 L383 299 L383 293 L377 293 L377 299 L372 299 L372 291 Z" fill="#0a72b9"/>
      <!-- globe -->
      <circle cx="380" cy="353" r="20" fill="#fff"/>
      <circle cx="380" cy="353" r="10" fill="#0a72b9"/>
      <path d="M375 347 q4 1 5 4 q-3 3 -6 1 z M382 355 q4 -1 5 2 q-2 4 -5 4 z" fill="#fff"/>
    </svg>
    <div class="brand-name">LeafCrest</div>
    <div class="contact-text person-name">Daniel Hartley</div>
    <div class="contact-text person-title">Managing Director</div>
    <div class="contact-text contact-line phone-line">555 010 2468</div>
    <div class="contact-text contact-line email-line">info@leafcrest.com</div>
    <div class="contact-text contact-line web-line">www.leafcrest.com</div>
  </section>
  <section class="card card-back">
    <div class="back-brand-name">LeafCrest</div>
  </section>
</div>
</body>
</html>
```